KP Rubbish Removal Business Card

Hey,
I need a double sided business card designed for a rubbish removal business based in Australia. Logo is already chosen, similar colours preferred for both sides of the business card.

Details to include:

Front:

KP Rubbish Removal
Darren Holloway
Managing Director
Mobile: 0471 920 246
Email: darren@kprubbishremoval.com.au
Website: kprubbishremoval.com.au

Rear:

How did we do?
kprubbishremoval.com.au/review

```html
<!DOCTYPE html>
<html lang="en">
<head>
<meta charset="utf-8">
<title>KP Rubbish Removal – Business Card</title>
<link rel="stylesheet" href="https://fonts.googleapis.com/css2?family=Montserrat:wght@600;700&family=Poppins:wght@500;600&family=Roboto:wght@400&display=swap">
<style>
  :root {
    --backdrop: #9a9a9a;
    --paper: #f4f4f3;
    --ink-dark: #3f3f40;
    --ink-soft: #6b6b6b;
    --brand-green: #1f8a48;
    --leaf-green: #4bb64a;
    --edge-green: #1c7a2a;
    --card-black: #0c0d0f;
    --white: #ffffff;
  }
  * { box-sizing: border-box; margin: 0; padding: 0; }
  html, body {
    width: 1200px; height: 1025px; overflow: hidden;
    background: var(--backdrop);
  }
  .sheet {
    width: 1200px; height: 1025px;
    display: flex; flex-direction: column; align-items: center; justify-content: center;
    gap: 40px;
  }
  .card {
    position: relative;
    width: 740px; height: 452px;
    border-bottom: 5px solid var(--edge-green);
    border-radius: 3px;
    overflow: hidden;
  }
  /* Front */
  .card--front {
    background: var(--paper);
    display: flex; align-items: center; justify-content: space-between;
    padding: 0 50px;
  }
  .contact { flex: none; margin-top: 30px; white-space: nowrap; }
  .contact__name {
    font-family: "Montserrat", sans-serif; font-weight: 700;
    font-size: 23px; letter-spacing: 0.5px; color: var(--brand-green);
    text-transform: uppercase; line-height: 1;
  }
  .contact__role {
    font-family: "Poppins", sans-serif; font-weight: 500;
    font-size: 18px; color: var(--ink-dark); margin-top: 4px;
  }
  .contact__list { list-style: none; margin-top: 14px; }
  .contact__item {
    display: flex; align-items: center; gap: 10px;
    font-family: "Roboto", sans-serif; font-size: 17px; color: var(--ink-soft);
    line-height: 1.6;
  }
  .contact__icon { width: 17px; height: 17px; flex: none; fill: none; stroke: var(--brand-green); stroke-width: 2; }
  .contact__icon--solid { fill: var(--brand-green); stroke: none; }
  .brand {
    flex: none; margin-top: -40px;
    display: flex; flex-direction: column; align-items: center; gap: 20px;
    white-space: nowrap;
  }
  .brand__dot {
    width: 120px; height: 120px; border-radius: 50%;
    background: var(--leaf-green);
  }
  .brand__name {
    font-family: "Poppins", sans-serif; font-weight: 600;
    font-size: 23px; letter-spacing: 0.5px; color: var(--ink-dark);
    text-transform: uppercase;
  }
  /* Back */
  .card--back {
    background: var(--card-black);
    display: flex; flex-direction: column; align-items: center; justify-content: center;
  }
  .back-brand {
    display: flex; flex-direction: column; align-items: center; gap: 16px;
  }
  .back-brand__dot {
    width: 140px; height: 140px; border-radius: 50%;
    background: var(--leaf-green);
  }
  .back-brand__name {
    font-family: "Montserrat", sans-serif; font-weight: 600;
    font-size: 20px; letter-spacing: 1px; color: var(--white);
    text-transform: uppercase; white-space: nowrap;
  }
  .review {
    margin-top: 24px; text-align: center; white-space: nowrap;
    font-family: "Montserrat", sans-serif; font-weight: 600;
    font-size: 27px; color: var(--white); text-transform: uppercase;
    line-height: 1.25; letter-spacing: 0.5px;
  }
</style>
</head>
<body>
<main class="sheet">
  <section class="card card--front" aria-label="Business card front">
    <div class="contact">
      <h1 class="contact__name">Darren Holloway</h1>
      <p class="contact__role">Managing Director</p>
      <ul class="contact__list">
        <li class="contact__item">
          <svg class="contact__icon contact__icon--solid" viewBox="0 0 24 24" aria-hidden="true"><path d="M6.6 10.8a15.1 15.1 0 0 0 6.6 6.6l2.2-2.2a1 1 0 0 1 1-.25 11.4 11.4 0 0 0 3.6.57 1 1 0 0 1 1 1V20a1 1 0 0 1-1 1A17 17 0 0 1 3 4a1 1 0 0 1 1-1h3.5a1 1 0 0 1 1 1c0 1.25.2 2.45.57 3.57a1 1 0 0 1-.25 1z"/></svg>
          0471 920 246
        </li>
        <li class="contact__item">
          <svg class="contact__icon" viewBox="0 0 24 24" aria-hidden="true"><rect x="2" y="5" width="20" height="14" rx="1"/><path d="M2 6l10 7 10-7"/></svg>
          darren@kprubbishremoval.com.au
        </li>
        <li class="contact__item">
          <svg class="contact__icon" viewBox="0 0 24 24" aria-hidden="true"><circle cx="12" cy="12" r="9"/><path d="M3 12h18M12 3c3 3 3 15 0 18M12 3c-3 3-3 15 0 18"/></svg>
          kprubbishremoval.com.au
        </li>
      </ul>
    </div>
    <div class="brand">
      <span class="brand__dot" aria-hidden="true"></span>
      <span class="brand__name">KP Rubbish Removal</span>
    </div>
  </section>

  <section class="card card--back" aria-label="Business card back">
    <div class="back-brand">
      <span class="back-brand__dot" aria-hidden="true"></span>
      <span class="back-brand__name">KP Rubbish Removal</span>
    </div>
    <p class="review">How did we do?<br>kprubbishremoval.com.au/review</p>
  </section>
</main>
</body>
</html>
```